Flyer-Design für Logistikdienstleister
Zielgruppe
Logistikdienstleister
Aufgabenstellung
Modern, Innovativ, Dienstleister, Kreativ, Automobil, Mittelstand

```html
<!DOCTYPE html>
<html lang="de">
<head>
<meta charset="utf-8">
<title>Finanzierung & Preisauskunft</title>
<link href="https://fonts.googleapis.com/css2?family=Open+Sans:wght@400;600;700&display=swap" rel="stylesheet">
<style>
:root{
  --red:#cf0d22;
  --red-text:#c8102e;
  --white:#ffffff;
  --grey:#636466;
  --grey-text:#555555;
  --stage:#efefef;
  --line:rgba(255,255,255,.75);
}
*{margin:0;padding:0;box-sizing:border-box}
html,body{width:1200px;height:882px;overflow:hidden}
body{background:var(--stage);font-family:"Open Sans",Arial,sans-serif;position:relative}
.stage{position:absolute;left:0;top:0;width:1280px;height:941px;transform:scale(0.9375);transform-origin:0 0}
.spread{position:absolute;left:81px;top:76px;width:1123px;height:794px;background:var(--red);overflow:hidden}
.page-left{position:absolute;left:0;top:0;width:559px;height:794px;background:var(--red)}
.page-right{position:absolute;left:559px;top:0;width:564px;height:794px}
.page-right svg.bg{position:absolute;left:0;top:0}
.heading{position:absolute;color:var(--white);font-weight:700;font-size:16px}
.subheading{position:absolute;left:36px;top:80px;color:var(--white);font-size:12.5px;white-space:nowrap}
.price-table{position:absolute;left:36px;top:107px;width:478px;border-collapse:collapse;color:var(--white);font-size:8px;line-height:1.3}
.price-table td,.price-table th{border-bottom:1px solid var(--line);padding:1.5px 5px;vertical-align:top;font-weight:400}
.price-table td+td{border-left:1px solid var(--line)}
.price-table thead th{background:#5e5e5e;text-align:left;height:10px;padding:0 5px;font-size:7.5px;border:none}
.price-table .num{text-align:right}
.price-table .pct{text-align:center}
.price-table .section td{background:var(--white);color:var(--red-text);text-align:center;font-size:11px;height:24px;vertical-align:bottom;padding-bottom:2px;border-left:none}
.price-table .total td{background:var(--white);color:var(--red-text);font-weight:700;height:24px;vertical-align:middle;border-left:none}
.price-table .total .label{text-align:right;font-size:11px}
.price-table .total .old{text-decoration:line-through;font-size:11px;text-align:right}
.price-table .total .new{font-size:15px;text-align:right;border-left:1px solid var(--red-text)}
.note{position:absolute;left:36px;top:428px;color:var(--white);font-size:9px;white-space:nowrap}
.options-title{position:absolute;left:10px;top:36px;color:var(--red-text);font-weight:700;font-size:15.5px}
.option{position:absolute;top:72px;width:130px;text-align:center;font-size:11.5px;line-height:1.3;color:var(--grey-text)}
.option .visual{width:60px;height:62px;margin:0 auto 18px;border-radius:8px;background:linear-gradient(160deg,#d9e1ea,#5d6b7b)}
.option h3{color:var(--red-text);font-size:12px;font-weight:700;margin:0}
.forms{position:absolute;left:79px;top:362px;color:var(--white);width:400px}
.forms h2,.info h2{font-size:15.5px;font-weight:700;margin-bottom:6px;white-space:nowrap}
.forms ol{list-style:none;font-size:12px;line-height:18px}
.forms ol li .marker{display:inline-block;width:13px}
.forms ol li .cont{padding-left:13px;display:block}
.info{position:absolute;left:79px;top:520px;color:var(--white)}
.info p{font-size:12px;margin-top:12px}
</style>
</head>
<body>
<div class="stage">
<div class="spread">
  <section class="page-left">
    <h1 class="heading" style="left:36px;top:50px">Beispiel Preisauskunft:</h1>
    <p class="subheading">Rotastore Typ 6 Basisrahmen + K2K GF Locker Zusatzrahmen – COMPLETE Software</p>
    <table class="price-table">
      <colgroup><col style="width:60px"><col style="width:216px"><col style="width:74px"><col style="width:50px"><col style="width:78px"></colgroup>
      <thead><tr><th>Artikel-ID</th><th>Beschreibung</th><th style="text-align:center">Listenpreis</th><th></th><th style="text-align:center">Aktions-Preis</th></tr></thead>
      <tbody>
        <tr class="section"><td colspan="5">HARD&nbsp; UND SOFTWARE</td></tr>
        <tr><td>0C4GR6-1</td><td>Rotastore Typ 6 Gen4, 13x36 Lagerorte-StandAlone, Complete Software</td><td class="num">17.600,00 €</td><td class="pct">5%</td><td class="num">16.720,00 €</td></tr>
        <tr><td>0218F</td><td>K2K GF Locker (6 Türen, schmal)</td><td class="num">1.837,50 €</td><td class="pct">5%</td><td class="num">1.745,63€</td></tr>
        <tr><td>0005P</td><td>Kontaktloser Kartenleser (RFID) (TAGX, LOCX)</td><td class="num">590,00€</td><td class="pct">5%</td><td class="num">560,50 €</td></tr>
        <tr><td>0400B</td><td>Standardfarbe - Dunkelblau (RAL 5010/4054)</td><td class="num">0,00 €</td><td class="pct">-</td><td class="num">0,00 €</td></tr>
        <tr class="section"><td colspan="5">VERPACKUNG UND VERSAND</td></tr>
        <tr><td>7980807U</td><td>Exportverpackung Rotastore 1150x1050x2050</td><td class="num">256,25 €</td><td class="pct">-</td><td class="num">256,25 €</td></tr>
        <tr><td>0301C</td><td>Exportverpackung - Schließfachschrank</td><td class="num">161,25 €</td><td class="pct">-</td><td class="num">161,25 €</td></tr>
        <tr><td>FRACHT</td><td>Kosten FRACHT</td><td class="num">320,00 €</td><td class="pct">-</td><td class="num">320,00 €</td></tr>
        <tr class="section"><td colspan="5">SERVICE UND SUPPORT</td></tr>
        <tr><td>SPECIAL</td><td>REMOTE Installations- und Inbetriebnahme Unterstützung</td><td class="num">685,00 €</td><td class="pct">-</td><td class="num">0,00 €</td></tr>
        <tr><td>SPECIAL</td><td>Wartungsvertrag C für den ersten SA Rotastore mit der Complete Software im Betrieb für 1 Jahr</td><td class="num">887,00 €</td><td class="pct">-</td><td class="num">0,00 €</td></tr>
        <tr><td>SPECIAL</td><td>Wartungsvertrag C/L für jeden weiteren Zusatzschrank/Rahmen (außer Rotastore) für 1 Jahr (gilt nur in Verbindung mit 0501A)</td><td class="num">61,00 €</td><td class="pct">-</td><td class="num">0,00 €</td></tr>
        <tr><td>0603A</td><td>DataLink Zugang pro Datenbank pro Jahr</td><td class="num">637,50 €</td><td class="pct">-</td><td class="num">0,00 €</td></tr>
        <tr class="total"><td colspan="2" class="label">Gesamt-Preis:</td><td class="old">25.027,50 €</td><td colspan="2" class="new">19.763,63 €</td></tr>
      </tbody>
    </table>
    <p class="note">Hierbei handelt es sich um eine Beispiel-Zusammensetzung unserer Produkte.</p>
  </section>

  <section class="page-right">
    <svg class="bg" width="564" height="794" viewBox="0 0 564 794" aria-hidden="true">
      <rect width="564" height="794" fill="var(--red)"/>
      <polygon points="0,0 564,0 564,360 0,294" fill="var(--white)"/>
      <polygon points="564,574 564,794 244,794" fill="var(--grey)"/>
    </svg>
    <h2 class="options-title">Finanzierungsoptionen:</h2>
    <div class="option" style="left:6px"><div class="visual" role="img" aria-label="Illustration: Person am Arbeitsplatz mit Bildschirm"></div><h3>OPTION 01:</h3>Verkauf von<br>Hard- und Software</div>
    <div class="option" style="left:143px"><div class="visual" role="img" aria-label="Illustration: Automat mit Person und Paketen"></div><h3>OPTION 02:</h3>Verkauf von<br>Hard- u. Software +<br>Lieferung der Artikel.</div>
    <div class="option" style="left:281px"><div class="visual" role="img" aria-label="Illustration: mehrere Automaten mit Person"></div><h3>OPTION 03:</h3>Verkauf von<br>Hard- u. Software +<br>Lieferung der Artikel,<br>sowie<br>Befüllung der<br>Automaten</div>
    <div class="option" style="left:419px"><div class="visual" role="img" aria-label="Illustration: Automatengruppe mit Techniker"></div><h3>100% Technischer Support durch den Hersteller Stockwell</h3></div>

    <div class="forms">
      <h2>Finanzierungsformen:</h2>
      <ol>
        <li><span class="marker">1.</span>Leasing</li>
        <li><span class="marker">2.</span>Finanzierung</li>
        <li><span class="marker">3.</span>Amortisation durch den Produktumsatz<span class="cont">in Verbindung mit Option 01.</span></li>
      </ol>
    </div>
    <div class="info">
      <h2>weitere Informationen zu den Produkten:</h2>
      <p>https://www.stockwell-systems.com/de/products</p>
    </div>
  </section>
</div>
</div>
</body>
</html>
```